PELMARK
stationery items
Professional
Karim Doulani
Managing Director
Corniva Plaza L27
Al Fannar Road
P.O. Box 58214
Dubai - UAE
kdoulani@pelmark-gulfa.com
www.pelmark-gulfa.com
looking for full stationery items (business cards, letter heads, envelopes)
LOGO
Strategy Think-tank & Real Estate Asset Management Solutions
full package of logo

```html
<!DOCTYPE html>
<html lang="en">
<head>
<meta charset="utf-8">
<title>Pelmark Stationery</title>
<link rel="stylesheet" href="https://fonts.googleapis.com/css2?family=Cormorant+Garamond:wght@600&family=Open+Sans:wght@400;600&display=swap">
<style>
  :root {
    --backdrop: #a6a8ab;
    --paper: #ffffff;
    --maroon: #7a1c21;
    --ink: #4a4a4c;
    --band: #6d6e71;
    --rule: #d9d9d9;
    --serif: "Cormorant Garamond", Georgia, serif;
    --sans: "Open Sans", Arial, sans-serif;
  }
  * { margin: 0; padding: 0; box-sizing: border-box; }
  html, body { width: 1200px; height: 684px; overflow: hidden; }
  body { background: var(--backdrop); position: relative; font-family: var(--sans); color: var(--ink); }

  .sheet { position: absolute; background: var(--paper); box-shadow: 0 1px 3px rgba(0,0,0,.25); }
  .wordmark { font-family: var(--serif); font-weight: 600; color: var(--maroon); letter-spacing: .08em; line-height: 1; }

  /* Letterhead */
  .letterhead { left: 199px; top: 17px; width: 435px; height: 645px; }
  .letterhead .wordmark { position: absolute; left: 24px; top: 44px; font-size: 22px; }
  .letterhead .contact { position: absolute; left: 24px; top: 600px; font-size: 5.5px; line-height: 8px; }
  .footer-rule { position: absolute; left: 0; right: 0; height: 2px; background: var(--maroon); }
  .footer-band { position: absolute; left: 0; right: 0; background: var(--band); color: #fff; font-size: 5px; padding-left: 24px; display: flex; align-items: center; }
  .letterhead .footer-rule { top: 632px; }
  .letterhead .footer-band { top: 636px; height: 9px; }

  /* Business card */
  .card-front { left: 41px; top: 216px; width: 156px; height: 125px; background: var(--maroon); }
  .card-front .wordmark { position: absolute; left: 0; right: 0; top: 48px; text-align: center; color: #fff; font-size: 20px; }
  .card-front .tagline { position: absolute; left: 0; right: 0; top: 101px; text-align: center; color: #fff; font-size: 4.6px; }
  .card-back { left: 41px; top: 343px; width: 156px; height: 135px; }
  .card-back .wordmark { position: absolute; left: 9px; top: 32px; font-size: 12px; }
  .card-back .person { position: absolute; left: 74px; top: 18px; }
  .card-back .name { font-family: var(--serif); font-weight: 600; color: var(--maroon); font-size: 9px; }
  .card-back .role { font-size: 4.6px; margin-bottom: 5px; }
  .card-back .lines { font-size: 4.3px; line-height: 6.4px; }
  .card-back .footer-rule { top: 111px; height: 1.5px; }
  .card-back .footer-band { top: 114px; height: 8px; font-size: 4px; padding-left: 9px; }

  /* Envelopes */
  .envelope-back { left: 643px; top: 103px; width: 533px; height: 235px; }
  .envelope-back svg { position: absolute; inset: 0; }
  .envelope-front { left: 643px; top: 362px; width: 533px; height: 233px; }
  .envelope-front .wordmark { position: absolute; left: 24px; top: 55px; font-size: 20px; }
  .envelope-front .contact { position: absolute; left: 24px; top: 158px; font-size: 5.5px; line-height: 8px; }
  .envelope-front .footer-rule { top: 205px; }
  .envelope-front .footer-band { top: 209px; height: 9px; }
</style>
</head>
<body>

<section class="sheet letterhead">
  <div class="wordmark">PELMARK</div>
  <div class="contact">
    <p>E kdoulani@pelmark-gulfa.com</p>
    <p>T +971 4 310 5820 &nbsp; F +971 4 310 5821</p>
    <p>A Corniva Plaza L27, Al Fannar Road, P.O. Box 58214 Dubai - UAE</p>
  </div>
  <div class="footer-rule"></div>
  <div class="footer-band">www.pelmark-gulfa.com</div>
</section>

<section class="sheet card-front">
  <div class="wordmark">PELMARK</div>
  <p class="tagline">Strategy Think-tank &amp; Real Estate Asset Management Solutions</p>
</section>

<section class="sheet card-back">
  <div class="wordmark">PELMARK</div>
  <div class="person">
    <p class="name">Karim Doulani</p>
    <p class="role">Managing Director</p>
    <div class="lines">
      <p>T +971 4 310 5820</p>
      <p>M +971 50 614 2207</p>
      <p>F +971 4 310 5821</p>
      <p>kdoulani@pelmark-gulfa.com</p>
      <p>Corniva Plaza L27</p>
      <p>Al Fannar Road</p>
      <p>P.O. Box 58214 Dubai - UAE</p>
    </div>
  </div>
  <div class="footer-rule"></div>
  <div class="footer-band">www.pelmark-gulfa.com</div>
</section>

<section class="sheet envelope-back">
  <svg width="533" height="235" viewBox="0 0 533 235">
    <path d="M2 2 L250 132 Q266 141 282 132 L531 2" fill="none" stroke="#c8c8c8" stroke-width="1"/>
  </svg>
</section>

<section class="sheet envelope-front">
  <div class="wordmark">PELMARK</div>
  <div class="contact">
    <p>E kdoulani@pelmark-gulfa.com</p>
    <p>T +971 4 310 5820 &nbsp; F +971 4 310 5821</p>
    <p>A Corniva Plaza L27, Al Fannar Road, P.O. Box 58214 Dubai - UAE</p>
  </div>
  <div class="footer-rule"></div>
  <div class="footer-band">www.pelmark-gulfa.com</div>
</section>

</body>
</html>
```